Brightwell Surface Care - Business Card Design

Use company logo and design a new business card. We are looking for a front and back design. The back should be a dark purple background. We want the back to show cartoon-like soap bubbles chasing mildew cartoon shaped figures. This gives the idea that Brightwell Surface Care provides exterior washing services that work. No mildew stands a chance when Brightwell Surface Care shows up to work. The mildew cartoon images should be green in color, have eyes, and look scared of the bubbles. The bubbles should be light blue in color and have eyes that looked excited to be there.
We will advertise on Mingleport and Pixelvine. These Mingleport and Pixelvine icons should be somewhere on the card.

```html
<!DOCTYPE html>
<html lang="en">
<head>
<meta charset="utf-8">
<title>Brightwell Surface Care – Business Card</title>
<link rel="stylesheet" href="https://fonts.googleapis.com/css2?family=Arimo:wght@400;700&display=swap">
<style>
  :root {
    --backdrop: #ececef;
    --purple: #3b2160;
    --purple-deep: #2f184f;
    --accent-blue: #5b74cc;
    --bubble-blue: #bfe3f7;
    --mildew-green: #7cc142;
    --white: #ffffff;
  }
  * { margin: 0; padding: 0; box-sizing: border-box; }
  html, body {
    width: 1200px; height: 1122px; overflow: hidden;
    background: var(--backdrop);
    font-family: "Arimo", Arial, sans-serif;
  }
  .sheet { position: relative; width: 1200px; height: 1122px; }
  .card {
    position: absolute; left: 150px; width: 900px; height: 500px;
    border-radius: 34px; overflow: hidden;
    box-shadow: 0 10px 30px rgba(0,0,0,.18);
  }
  .card--back { top: 40px; background: var(--purple); }
  .card--front { top: 582px; background: var(--white); }

  .character-field {
    position: absolute; inset: 0;
    background:
      radial-gradient(circle at 16% 20%, rgba(191,227,247,.55) 0 6%, transparent 6.5%),
      radial-gradient(circle at 62% 12%, rgba(191,227,247,.55) 0 5%, transparent 5.5%),
      radial-gradient(circle at 88% 38%, rgba(191,227,247,.55) 0 5%, transparent 5.5%),
      radial-gradient(circle at 28% 84%, rgba(191,227,247,.55) 0 5.5%, transparent 6%),
      radial-gradient(circle at 30% 14%, rgba(124,193,66,.6) 0 5%, transparent 5.5%),
      radial-gradient(circle at 86% 12%, rgba(124,193,66,.6) 0 5%, transparent 5.5%),
      radial-gradient(circle at 10% 70%, rgba(124,193,66,.6) 0 5%, transparent 5.5%),
      radial-gradient(circle at 84% 82%, rgba(124,193,66,.6) 0 7%, transparent 7.5%);
  }
  .brand {
    position: absolute; left: 0; right: 0; top: 190px;
    text-align: center; color: var(--white);
    font-weight: 700; font-size: 58px; letter-spacing: .5px; line-height: 1.1;
  }
  .social {
    position: absolute; left: 0; right: 0; top: 330px;
    display: flex; justify-content: center; gap: 34px;
  }
  .social__item {
    display: flex; align-items: center; gap: 10px;
    color: var(--white); font-size: 20px;
  }
  .social__dot { width: 30px; height: 30px; border-radius: 50%; background: var(--accent-blue); }

  .front-art { position: absolute; inset: 0; }
  .front-brand {
    position: absolute; left: 50px; top: 205px; width: 330px;
    color: var(--purple); font-weight: 700; font-size: 44px; line-height: 1.1;
  }
  .contact {
    position: absolute; right: 46px; top: 70px; width: 390px;
    text-align: right; color: var(--white);
  }
  .contact__name { color: var(--accent-blue); font-weight: 700; font-size: 38px; letter-spacing: .5px; }
  .contact__role { font-size: 24px; margin-top: 4px; }
  .contact__list { list-style: none; margin-top: 34px; font-size: 21px; line-height: 1.45; }
  .contact__list li { display: flex; justify-content: flex-end; align-items: center; gap: 12px; }
  .contact__list .gap { margin-top: 14px; }
  .icon { width: 18px; height: 18px; flex: none; }
  .icon--blank { visibility: hidden; }
</style>
</head>
<body>
<main class="sheet">

  <section class="card card--back" aria-label="Card back">
    <div class="character-field" role="img" aria-label="Cartoon light blue soap bubbles with excited eyes chasing scared green mildew characters"></div>
    <div class="brand">Brightwell<br>Surface Care</div>
    <div class="social">
      <span class="social__item"><span class="social__dot"></span>Mingleport</span>
      <span class="social__item"><span class="social__dot"></span>Pixelvine</span>
    </div>
  </section>

  <section class="card card--front" aria-label="Card front">
    <svg class="front-art" viewBox="0 0 900 500" aria-hidden="true">
      <path d="M372 0 C560 120 600 330 470 500 L900 500 L900 0 Z" fill="var(--purple)"/>
      <path d="M360 0 C545 120 585 330 455 500 L435 500 C560 330 520 120 330 0 Z" fill="var(--white)"/>
      <path d="M420 40 C560 160 570 360 440 500 L395 500 C530 350 520 170 400 40 Z" fill="var(--accent-blue)"/>
      <path d="M335 0 C450 60 500 120 520 180 C490 110 420 50 320 0 Z" fill="var(--purple)"/>
    </svg>
    <div class="front-brand">Brightwell<br>Surface Care</div>
    <div class="contact">
      <div class="contact__name">DANIEL HARTLEY</div>
      <div class="contact__role">Founder &amp; CEO</div>
      <ul class="contact__list">
        <li>Your Address, City
          <svg class="icon" viewBox="0 0 20 20"><path d="M10 1a6 6 0 0 1 6 6c0 5-6 12-6 12S4 12 4 7a6 6 0 0 1 6-6z" fill="var(--accent-blue)"/><circle cx="10" cy="7" r="2.2" fill="var(--purple)"/></svg></li>
        <li>State, Zip 1235 <svg class="icon icon--blank" viewBox="0 0 20 20"></svg></li>
        <li class="gap">(123) 456-7890
          <svg class="icon" viewBox="0 0 20 20"><path d="M4 2l3 0 2 4-2 2a10 10 0 0 0 5 5l2-2 4 2v3a2 2 0 0 1-2 2A16 16 0 0 1 2 4a2 2 0 0 1 2-2z" fill="var(--accent-blue)"/></svg></li>
        <li>(123) 456-7890
          <svg class="icon" viewBox="0 0 20 20"><rect x="5" y="1" width="10" height="18" rx="2" fill="none" stroke="var(--accent-blue)" stroke-width="2"/><circle cx="10" cy="15.5" r="1.2" fill="var(--accent-blue)"/></svg></li>
        <li>hello@brightwellcare.example
          <svg class="icon" viewBox="0 0 20 20"><rect x="1" y="4" width="18" height="12" rx="1" fill="var(--accent-blue)"/><path d="M1 4l9 7 9-7" fill="none" stroke="var(--purple)" stroke-width="1.5"/></svg></li>
        <li>brightwellcare.example
          <svg class="icon" viewBox="0 0 20 20"><circle cx="10" cy="10" r="8" fill="none" stroke="var(--accent-blue)" stroke-width="2"/><path d="M2 10h16M10 2c-4 4-4 12 0 16M10 2c4 4 4 12 0 16" fill="none" stroke="var(--accent-blue)" stroke-width="1.5"/></svg></li>
      </ul>
    </div>
  </section>

</main>
</body>
</html>
```